Indie Alternative band needs a CD Cover Design for its second album.

We need a CD Cover Design for the second album of our Indie Alternative band, with the album name to be called "Vatrel". We would like to see minimalist illustration-based clean and professional designs inspired by the published design samples provided. 1) The design has a "looking into the horizon" angle perspective (4.jpg). 2) It will feature cumulus / puffy clouds at the top and supporting the imagery of the couple in the middle. 3) Then these clouds are reflected at the bottom. (1.jpg). 4) The clouds will mainly form in the middle (see 4c.jpg)... 5) The ground where the clouds are reflected should not be water, but more like a reflective glass. (3.jpg)... 6) There is a bright white line in the middle to mark the invisible horizon line (see "bright horizon line")... 7) At the middle of the horizon, there will be 2 people (light colored skin) looking at each other but not touching or holding each other: a boy at the left, and a girl at the right. (follow how they look at: "couple.jpg" and "2.jpg"). The boy has dark hair and dark pants with light colored sleeves, similar to the guy on the first album (first album.jpg). 8) Design will mainly use bright masculine blue and colors, and because it's our second album will symbolically show the number "2" (e.g. 2 people, 2 sets of clouds at the top and bottom). 9) The design will continue the story theme from the first album design. The final design should communicate the ongoing musical journey of the band, symbolized through the minimal design elements mentioned here, e.g. boy enters this new world from album 1, then boy meets this girl inside this new world from this album 2. All things being equal design-wise, we may consider a design that has a similar look and feel as our first album for reason of consistency.

Target Market(s)

Music fans of the indie alternative genre.

Industry/Entity Type

Entertainment Industry

Font styles to use
Sans Serif

Colors

Designer to choose colors to be used in the design.

Requirements
Must have
• * The words "Moss Fernway" at the top and "Vatrel" at the bottom, which is the band name and album name, respectively. See "first album.jpg".
• * A minimalist design layout, very clean and focused on the design elements mentioned.
• * The illustrated clouds must look natural and random and not duplicated patterns. But it’s volume and amount needs to be similar to 4c.jpg.
• * The 5 main design elements: 1) a horizon angled look and feel, 2) puffy clouds at the top (see 4c.jpg), 3) reflected clouds at the bottom, 4) 2 people in the middle as the center focus of the design. 5) a bright, straight line in the middle - see "1.jpg"
• * Using bright masculine blue as the main color.
• * The boy needs to have dark hair and dark pants with long and light colored sleeves - similar to the guy on the first album (first album.jpg).
• * Size is at least 1600 x 1600 pixels and at least 300 dpi.
Nice to have
• * Minimalist illustrations close to the published samples provided.
• * The clouds used in the design needs to be puffy and not thin (see 4c.jpg). But it will be faded a little out so as not to grab too much attention away from the 2 people in the middle.
• * Similar Font Type, just like from the first album (first album.jpg).
• * Ground look showing reflected clouds that is bright and shiny without it looking like water.
Should not have
• * Copying the published copyrighted sample designs. Please provide original illustrations and designs.
• * The boy and girl must not touch each other, but they are looking at each other. See "2.jpg" and "couple.jpg".
• * Too many design elements, needs to have a minimalist type of design
• * Too dark and gloomy look and feel
• * Dark colors
• * Thin looking clouds that are scattered. See "4c.jpg" on clouds formation to follow.
• * Design that is placed on a CD cover and disc. Or a design that is a duplicate of an already submitted design except that is has been placed on a CD cover and disc.

```html
<!DOCTYPE html>
<html lang="en">
<head>
<meta charset="UTF-8">
<title>Moss Fernway — Vatrel</title>
<link rel="stylesheet" href="https://fonts.googleapis.com/css2?family=Oswald:wght@300;400&display=swap">
<style>
  :root {
    --sky-violet: #7b79b3;
    --sky-deep: #5f5d98;
    --sky-mist: #9a98c8;
    --cloud-white: #e6e4ef;
    --cloud-shade: #b9b7d4;
    --portal-teal: #5fdcbf;
    --horizon-glow: rgba(235, 235, 255, 0.55);
    --ink: #0c0c14;
    --figure-dark: #4a4a5c;
    --figure-blush: #b49aa6;
  }

  html, body {
    margin: 0;
    padding: 0;
    width: 1200px;
    height: 1200px;
    overflow: hidden;
    background: var(--sky-violet);
  }

  .cover {
    position: relative;
    width: 1200px;
    height: 1200px;
    overflow: hidden;
  }

  .sky-scene {
    position: absolute;
    inset: 0;
    background:
      radial-gradient(ellipse 380px 130px at 170px 150px, rgba(230,228,239,0.75), transparent 70%),
      radial-gradient(ellipse 420px 150px at 930px 170px, rgba(230,228,239,0.8), transparent 70%),
      radial-gradient(ellipse 360px 110px at 960px 320px, rgba(220,218,236,0.6), transparent 70%),
      radial-gradient(ellipse 300px 90px at 260px 320px, rgba(200,198,226,0.45), transparent 70%),
      radial-gradient(ellipse 380px 130px at 170px 1040px, rgba(230,228,239,0.65), transparent 70%),
      radial-gradient(ellipse 420px 150px at 960px 1010px, rgba(230,228,239,0.7), transparent 70%),
      radial-gradient(ellipse 360px 110px at 950px 870px, rgba(220,218,236,0.5), transparent 70%),
      linear-gradient(180deg, var(--sky-mist) 0%, var(--sky-violet) 35%, var(--sky-deep) 49%, var(--sky-violet) 51%, var(--sky-violet) 65%, var(--sky-mist) 100%);
  }

  .horizon-line {
    position: absolute;
    left: 0;
    right: 0;
    top: 586px;
    height: 1px;
    background: var(--horizon-glow);
  }

  .portal-frame {
    position: absolute;
    left: 423px;
    top: 316px;
    width: 311px;
    height: 664px;
    box-sizing: border-box;
    border: 2px solid var(--portal-teal);
    box-shadow: 0 0 10px rgba(95, 220, 191, 0.45), inset 0 0 14px rgba(95, 220, 191, 0.2);
    background: rgba(150, 150, 205, 0.18);
  }

  .couple {
    position: absolute;
    left: 492px;
    top: 372px;
    width: 190px;
    height: 286px;
    border-radius: 40px 40px 6px 6px;
    background: linear-gradient(90deg, var(--figure-dark) 0%, var(--figure-dark) 45%, transparent 50%, var(--figure-blush) 55%, var(--figure-blush) 100%);
    opacity: 0.55;
  }

  .couple-reflection {
    position: absolute;
    left: 492px;
    top: 660px;
    width: 190px;
    height: 284px;
    border-radius: 6px 6px 40px 40px;
    background: linear-gradient(90deg, var(--figure-dark) 0%, var(--figure-dark) 45%, transparent 50%, var(--figure-blush) 55%, var(--figure-blush) 100%);
    opacity: 0.3;
  }

  .band-name,
  .album-title {
    position: absolute;
    left: 0;
    right: 0;
    margin: 0;
    text-align: center;
    font-family: "Oswald", "Arial Narrow", sans-serif;
    font-weight: 400;
    color: var(--ink);
    text-transform: uppercase;
    line-height: 1;
  }

  .band-name {
    top: 162px;
    font-size: 58px;
    letter-spacing: 0.62em;
    padding-left: 0.62em;
  }

  .album-title {
    top: 1042px;
    font-size: 58px;
    letter-spacing: 0.62em;
    padding-left: 0.62em;
  }
</style>
</head>
<body>
  <main class="cover">
    <div class="sky-scene" role="img" aria-label="Puffy white clouds over a starry violet sky, mirrored on a glossy glass floor"></div>
    <div class="horizon-line"></div>
    <div class="portal-frame"></div>
    <div class="couple" role="img" aria-label="A young man in a dark sweater and a red-haired woman in a pale pink dress standing apart, looking at each other"></div>
    <div class="couple-reflection" role="img" aria-label="Reflection of the couple on the glass floor"></div>
    <h1 class="band-name">Moss Fernway</h1>
    <h2 class="album-title">Vatrel</h2>
  </main>
</body>
</html>
```